KRL Brochure

I'm looking to update and make easier to read our brochure. I uploaded our current brochure and logo.

Target Market(s)

Brides

Requirements
Must have
• same or similar text as in old brochure

```html
<!DOCTYPE html>
<html lang="en">
<head>
<meta charset="utf-8">
<title>KRL Productions Brochure</title>
<link rel="stylesheet" href="https://fonts.googleapis.com/css2?family=Arimo:wght@400&family=Roboto:wght@300;400;500&family=Cormorant+Garamond:ital,wght@1,600&display=swap">
<style>
  :root {
    --page-bg: #ece9e4;
    --navy-light: #5069b6;
    --navy-dark: #1e2c5e;
    --band-blue: #4b64b4;
    --ink: #2e2e2e;
    --white: #ffffff;
    --strip-black: #0b0b0b;
    --link-blue: #4a63b3;
    --ornament: #d5d9ea;
  }
  * { box-sizing: border-box; margin: 0; padding: 0; }
  html, body { width: 1200px; height: 943px; overflow: hidden; background: var(--page-bg); }
  .brochure {
    position: absolute; left: 35px; top: 35px; width: 1128px; height: 872px;
    display: flex; box-shadow: 0 4px 14px rgba(0,0,0,.25);
  }
  .panel { position: relative; height: 100%; }

  /* About panel */
  .panel-about {
    width: 375px; padding: 24px 22px 0 23px;
    background: linear-gradient(120deg, var(--navy-light) 0%, #3d54a0 45%, var(--navy-dark) 100%);
    color: var(--white); font-family: "Arimo", Arial, sans-serif;
  }
  .about-copy p { font-size: 15px; line-height: 27px; text-align: justify; margin-bottom: 27px; }
  .tagline {
    font-family: "Cormorant Garamond", Georgia, serif; font-style: italic; font-weight: 600;
    font-size: 29px; line-height: 40px; margin-top: 30px; margin-left: 5px;
  }
  .tagline .slowly { display: block; margin-top: 40px; }
  .credits { position: absolute; left: 0; right: 0; bottom: 23px; text-align: center; font-size: 15px; line-height: 21px; }

  /* Services panel */
  .panel-services { width: 378px; font-family: "Roboto", Arial, sans-serif; font-weight: 300; color: var(--ink); }
  .services-photo {
    position: absolute; inset: 0;
    background: linear-gradient(160deg, #f4f4f4 0%, #e4e4e4 35%, #cfcfcf 60%, #eeeeee 100%);
  }
  .services-list { position: relative; list-style: none; padding: 52px 0 0 36px; }
  .services-list li { font-size: 22px; line-height: 53px; position: relative; padding-left: 24px; }
  .services-list li::before {
    content: ""; position: absolute; left: 0; top: 23px; width: 7px; height: 7px; border-radius: 50%; background: var(--ink);
  }
  .contact { position: absolute; left: 0; right: 0; top: 508px; text-align: center; font-size: 18px; line-height: 24px; }
  .contact .address { margin-top: 24px; }
  .contact .office + .office { margin-top: 24px; }
  .contact .phone { margin-top: 24px; }

  /* Wordmark */
  .wordmark { display: flex; align-items: center; justify-content: center; gap: 12px; }
  .wordmark-dot { width: 26px; height: 26px; border-radius: 50%; background: var(--band-blue); }
  .wordmark-name { font-family: "Roboto", Arial, sans-serif; font-weight: 500; font-size: 34px; line-height: 1; color: #222; letter-spacing: .5px; }

  /* Cover panel */
  .panel-cover { width: 375px; background: var(--white); }
  .cover-strip { position: absolute; left: 0; top: 0; width: 42px; height: 100%; background: var(--strip-black); }
  .cover-logo { position: absolute; left: 42px; right: 0; top: 55px; }
  .ornament { position: absolute; left: 60px; width: 292px; height: 74px; background: var(--ornament); border-radius: 37px; opacity: .7; }
  .ornament-top { top: 142px; }
  .ornament-bottom { top: 316px; }
  .title-band {
    position: absolute; left: 42px; right: 0; top: 218px; height: 97px; background: var(--band-blue);
    color: var(--white); font-family: "Roboto", Arial, sans-serif; font-weight: 300;
    font-size: 35px; line-height: 37px; text-align: center; padding-top: 13px;
  }
  .couple-photo {
    position: absolute; left: 60px; top: 415px; width: 295px; height: 457px;
    background: linear-gradient(180deg, #3f5a2c 0%, #5a7040 30%, #2a2a2a 65%, #e9e9ea 100%);
  }
  .login-band {
    position: absolute; left: 2px; right: 20px; top: 797px; height: 48px; background: var(--white);
    color: var(--link-blue); font-family: "Roboto", Arial, sans-serif; font-weight: 300; font-size: 26px;
    text-align: center; line-height: 48px;
  }
</style>
</head>
<body>
<main class="brochure">
  <section class="panel panel-about">
    <div class="about-copy">
      <p>Since 1995 for mission at KRL Production has been simple, to preserve the special moments of your wedding day in the most unobtrusive, discreet manner possible. Using hand held cameras and small lights allows us to blend in rather than stick out.</p>
      <p>We pride ourselves on personal service and going the extra mile for our clients. Each wedding is unique and our style reflects that individuality. We take personal pride in every video we create. We have thousands of satisfied clients who love our works and would recommend us to their closest friends and family.</p>
      <p>Video technology changes every day. We strive to stay ahead of the trend making sure you get a video you will enjoy just as much 20 yers from now as you do today.</p>
    </div>
    <p class="tagline">Relive the fastest day<br>of your life...<span class="slowly">Slowly</span></p>
    <p class="credits">Photo by Harbor Photo Group<br>All Major Credit Cards Accepted</p>
  </section>

  <section class="panel panel-services">
    <div class="services-photo" role="img" aria-label="Soft black and white photo of a bride's gown being laced up"></div>
    <ul class="services-list">
      <li>Quality Ditital Equipment</li>
      <li>Unobtrusive</li>
      <li>Professional Saff</li>
      <li>Cutom Packages</li>
      <li>Photography Available</li>
      <li>Aerial Video</li>
    </ul>
    <div class="contact">
      <div class="wordmark"><span class="wordmark-dot"></span><span class="wordmark-name">KRL PRODUCTIONS</span></div>
      <div class="address">
        <p class="office">Maple Ridge Office<br>48 Orchard Rd.<br>Maple Ridge, CT 06810</p>
        <p class="office">Lakeside Office<br>12 Harbor Ln<br>Lakeside, CT 06880</p>
      </div>
      <p class="phone">203-555-0142<br>www.krlstudio.com</p>
    </div>
  </section>

  <section class="panel panel-cover">
    <div class="cover-strip"></div>
    <div class="cover-logo wordmark"><span class="wordmark-dot"></span><span class="wordmark-name">KRL PRODUCTIONS</span></div>
    <div class="ornament ornament-top" role="img" aria-label="Decorative scroll flourish"></div>
    <h1 class="title-band">Best Wedding<br>Photography</h1>
    <div class="ornament ornament-bottom" role="img" aria-label="Decorative scroll flourish"></div>
    <div class="couple-photo" role="img" aria-label="Portrait photo of a smiling bride and groom in front of green hedges"></div>
    <p class="login-band">Log On www.krlstudio.com</p>
  </section>
</main>
</body>
</html>
```